Wine Label named: Five Lanterns

We are a wine producer, who wishes to launch a new premium wine called: Five Lanterns
Our winery is situated in a rolling hill, with slopes, where Five Lanterns exists in the property. One dates to the 15th century and the other more recent to the 18th century. Its a unique feature of the winery and we wish to create a label that represents these, but is NOT religious! Difficult task I know. Think you can pull it off? Let us see it! We start with one label, but the winner will have 5 more labels to design.

Target Market(s)

30-50 year old men

Industry/Entity Type

Wine

Colors

Designer to choose colors to be used in the design.

Requirements
Must have
• serious look and premium feel. name of the wine: Five Lanterns
Nice to have
• 2019 14% ABV
Should not have
• a religious look and feel

```html
<!DOCTYPE html>
<html lang="en">
<head>
<meta charset="utf-8">
<title>Five Lanterns – Red Wine Label</title>
<link rel="stylesheet" href="https://fonts.googleapis.com/css2?family=Josefin+Sans:wght@400;600&display=swap">
<style>
  :root {
    --page: #ffffff;
    --label-black: #0c0c0d;
    --cream: #fbf0df;
    --gold: #e8d29c;
    --frame-gold: #b8995c;
    --band-wine: #751f32;
    --band-text: #f6ead6;
    --scene-sky: #f6e6c8;
    --scene-hill: #c9a24e;
    --scene-vine: #6f7a3c;
  }
  * { box-sizing: border-box; margin: 0; padding: 0; }
  html, body {
    width: 1200px;
    height: 825px;
    overflow: hidden;
    background: var(--page);
  }
  .canvas {
    position: relative;
    width: 1200px;
    height: 825px;
  }
  .label {
    position: absolute;
    left: 358px;
    top: 36px;
    width: 482px;
    height: 756px;
    background: var(--label-black);
    font-family: "Josefin Sans", sans-serif;
    text-align: center;
  }
  .estd-row {
    position: absolute;
    top: 50px;
    left: 0;
    width: 100%;
    display: flex;
    justify-content: center;
    align-items: center;
    gap: 14px;
    color: var(--cream);
    font-size: 13px;
    letter-spacing: 1.5px;
  }
  .brand-mark {
    display: flex;
    align-items: center;
    gap: 6px;
    color: var(--cream);
    font-size: 13px;
    letter-spacing: 1.5px;
  }
  .brand-mark .square {
    width: 10px;
    height: 10px;
    background: var(--band-wine);
  }
  .wine-name {
    position: absolute;
    top: 112px;
    left: 0;
    width: 100%;
    color: var(--cream);
    font-weight: 400;
    font-size: 62px;
    line-height: 76px;
    letter-spacing: 7px;
    padding-left: 7px;
  }
  .vineyard-scene {
    position: absolute;
    left: 68px;
    top: 272px;
    width: 346px;
    height: 358px;
    border: 2px solid var(--frame-gold);
    background: linear-gradient(180deg,
      var(--scene-sky) 0%,
      #f1dcb4 26%,
      #a99a55 38%,
      var(--scene-hill) 58%,
      var(--scene-vine) 80%,
      #8d8140 100%);
  }
  .wine-type {
    position: absolute;
    top: 650px;
    left: 0;
    width: 100%;
    color: var(--cream);
    font-size: 27px;
    letter-spacing: 1.5px;
  }
  .info-band {
    position: absolute;
    left: 0;
    bottom: 0;
    width: 100%;
    height: 55px;
    background: var(--band-wine);
    display: flex;
    align-items: center;
    justify-content: space-between;
    padding: 0 50px 0 34px;
    color: var(--band-text);
    font-weight: 600;
    font-size: 15px;
    letter-spacing: 1.8px;
  }
  .info-band .divider {
    width: 3px;
    height: 26px;
    background: var(--frame-gold);
  }
</style>
</head>
<body>
  <main class="canvas">
    <section class="label">
      <div class="estd-row">
        <span class="estd">ESTD</span>
        <span class="brand-mark"><span class="square"></span>FIVE LANTERNS</span>
        <span class="year">2019</span>
      </div>
      <h1 class="wine-name">FIVE<br>LANTERNS</h1>
      <div class="vineyard-scene" role="img" aria-label="Photograph of rolling vineyard hills at golden hour with two small white estate buildings among the vines"></div>
      <p class="wine-type">Red Wine</p>
      <div class="info-band">
        <span class="abv">14% ABV</span>
        <span class="divider"></span>
        <span class="origin">MADE IN SPAIN</span>
        <span class="divider"></span>
        <span class="volume">70cl</span>
      </div>
    </section>
  </main>
</body>
</html>
```